Fable Organics Label Project- Updates made to project!

Project Scope: Branding opportunity for internet based skin care line. Design coordinating label for 4 different products. Each design shall be editable in Adobe Illustrator as a template including all fonts, symbols, and guides. Submit a design for all 4 products (preferably together as it would look on a retail shelf), business card, and logo.
Cleanser: STEP 1 Label Size: 5 x 4.5 inches (w x h) LULL CLEANSER
Toner: STEP 2 Label Size: 5 x 4.5 inches (w x h) HUSHWAY TONER- A piece of each crystal sits at the bottom of each solution. It coordinates with the "Calm Within" of our logo.
Serum STEP 3 Label Size: Label Size: 4.25 x 2.25 ANTI-AGING SERUM
Moisturizer: STEP 4 Label Size: Label Size: 1”x7.25” MOISTURIZER
Each label needs to include:
Front:
Attractive larger sized STEP #
Logo
Product name and short description
Decorative design Symbol(s)
Back:
Area on back to say short description
Directions for use
Larger area for ingredients
Website: www.fableorganics-example.com
Address of distribution
Barcode

Fable Skin Care, an esthetician created line provides organic and natural based products for all skin types. With an emphasis on anti-aging, this simple 4- step system can be used by many including pregnant and oncology consumers. The unique thing about our line is that the toners and serums contain crystals such as amethyst and rose quarts to promote inner peace as well as outer beauty. Each product is handmade with natural, quality ingredients and are 70-90% Organic.
Target Market: Women ages 30-45 years old. This demographic is on the go, and wants a simple-easy to read label, & a skin care system that addresses her concerns. Just as this consumer is mindful of her fitness and what she puts in her body, she tends to purchase environmentally friendly, and natural products. Health and wellness trends reflect this, as organic beauty products are expected to grow 74% from 2013 to 2018. She enjoys meditation and yoga, and she is curious about eastern medicine holistic healing trends.

Company Name: Fable Skin Care
Tagline: Calm Within- Glow Without
Package Feel: Simple, elegant easy to read step on each product. STEP 1: AM/PM. Attractive numbering. A symbol that reflects the brand. Not necessarily a Jewel or Crystal because the name speaks for itself. Beautiful, soft, eye catching design that draws the consumer to pick it up. Clear or white label welcomed. Some color palettes provided.
Descriptive words the packaging should represent: Yoga, Zen, mystic, eye catching, healing energy, natural, quality ingredients, sophisticated, beautiful, serenity, easy to read- bold-attractive numbering on front.
Inspiration Brands: KAVU Organics- Beautiful watercolor packaging that resonates a "feeling"

Attached are pictures of the packaging, inspirational pictures, skin care lines that are attractive, ect.

Packaging SPECS:

Cleanser:
Color Clear
Size 4 oz
Material PET
Case Pack
Neck Finish 24-410
Diameter 1.58 in / 4.013 cm
Height 6 in / 15.240 cm
Label Dimensions 5x4.5
Print Dimensions 5x4.5
Print Dimensions in (diameter)

TONER BOTTLE: Same as above

SERUM BOTTLE:
Color Clear
Size 2 oz
Material PET
Neck Finish 20-410
Diameter 1.358 in / 3.449 cm
Height 3.274 in / 8.316 cm

Moisturizer:
2.3 oz
Height:53 mm
Diameter: 60 mm
Neck: 58/400

Target Market(s)

Women ages 30-45 years old. This demographic is on the go, and wants a simple-easy to read label, & a skin care system that addresses her concerns. Just as this consumer is mindful of her fitness and what she puts in her body, she tends to purchase environmentally friendly, and natural products. Health and wellness trends reflect this, as organic beauty products are expected to grow 74% from 2013 to 2018. She enjoys meditation and yoga, and she is curious about eastern medicine holistic healing trends.

Industry/Entity Type

Skin Care Product

Contact Information for Business Card

Details given upon completion.

Logo Text

Fable Organics Calm Within- Glow Without

Requirements
Must have
• A large step number on the front. Coordinating symbols and colors. Must have a professional retail look and be easy to read.
Nice to have
• Clean, simple, eye catching packaging. Watercolor designs. Designs that inspire "feelings" www.kavuorganics-example.com

```html
<!DOCTYPE html>
<html lang="en">
<head>
<meta charset="utf-8">
<title>Fable Skin Care – Label System</title>
<link rel="stylesheet" href="https://fonts.googleapis.com/css2?family=Archivo+Black&family=Archivo:wght@400;700;800&family=Raleway:wght@200;300&family=Oswald:wght@600&display=swap">
<style>
  :root {
    --ink: #0a0a0a;
    --paper: #ffffff;
    --label-teal: #c4e8e8;
    --label-teal-light: #dbf1f0;
    --label-teal-deep: #a9dcdc;
    --label-edge: #c9c6c4;
    --text-grey: #4a4a4a;
    --tagline-teal: #b9e6ea;
    --icon-teal: #4fbfc1;
    --icon-blue: #2f8fc9;
    --icon-grey: #3f3f3f;
    --swatch-1: #b6b5b9;
    --swatch-2: #e2e3e8;
    --swatch-3: #f9f8f5;
    --swatch-4: #f6ede7;
    --swatch-5: #e8dad0;
  }
  * { box-sizing: border-box; margin: 0; padding: 0; }
  html, body { width: 1200px; height: 1034px; overflow: hidden; background: var(--paper); }
  .canvas { position: relative; width: 1200px; height: 1034px; overflow: hidden; background: var(--paper); font-family: "Archivo", sans-serif; color: var(--ink); }

  /* product labels */
  .label {
    position: absolute;
    background: linear-gradient(160deg, var(--label-teal-light) 0%, var(--label-teal) 45%, var(--label-teal-deep) 75%, var(--label-teal-light) 100%);
    text-align: center;
  }
  .label::before, .label::after {
    content: ""; position: absolute; left: 0; right: 0; height: 14px;
    background: linear-gradient(90deg, var(--label-edge), var(--swatch-2), var(--swatch-4), var(--label-edge));
  }
  .label::before { top: 0; }
  .label::after { bottom: 0; }
  .label--cleanser { left: 70px; top: 486px; width: 248px; height: 458px; }
  .label--toner { left: 382px; top: 372px; width: 212px; height: 578px; }

  .mark-circle { position: absolute; left: 50%; transform: translateX(-50%); border: 3px solid var(--ink); border-radius: 50%; }
  .label .mark-circle { width: 84px; height: 84px; }
  .label--cleanser .mark-circle { top: 29px; }
  .label--toner .mark-circle { top: 40px; }

  .wordmark { position: absolute; left: 0; right: 0; font-family: "Archivo Black", sans-serif; letter-spacing: 0.62em; text-indent: 0.62em; line-height: 1; }
  .subbrand { position: absolute; left: 0; right: 0; font-weight: 800; letter-spacing: 0.16em; line-height: 1; }
  .label--cleanser .wordmark { top: 135px; font-size: 31px; }
  .label--cleanser .subbrand { top: 167px; font-size: 17px; }
  .label--toner .wordmark { top: 151px; font-size: 28px; }
  .label--toner .subbrand { top: 180px; font-size: 16px; }

  .tag-band { position: absolute; left: 0; right: 0; background: var(--ink); display: flex; align-items: center; justify-content: center; gap: 14px; }
  .tag-band .dot { border: 1.5px solid var(--tagline-teal); border-radius: 50%; flex: none; }
  .tag-band .tagline { font-family: "Raleway", sans-serif; font-weight: 300; color: var(--tagline-teal); text-align: left; line-height: 1.05; }
  .label--cleanser .tag-band { top: 193px; height: 49px; }
  .label--cleanser .dot { width: 32px; height: 32px; }
  .label--cleanser .tagline { font-size: 17px; }
  .label--toner .tag-band { top: 206px; height: 46px; }
  .label--toner .dot { width: 30px; height: 30px; }
  .label--toner .tagline { font-size: 15px; }

  .info { position: absolute; left: 0; right: 0; font-size: 12px; color: var(--text-grey); letter-spacing: 0.06em; line-height: 14px; }
  .label--cleanser .info { top: 256px; }
  .label--toner .info { top: 365px; }

  .product-box { position: absolute; left: 50%; transform: translateX(-50%); border: 3px solid var(--ink); background: var(--paper); }
  .product-name { font-weight: 800; letter-spacing: 0.17em; display: flex; align-items: center; justify-content: center; }
  .step-bar { background: var(--ink); color: var(--paper); display: flex; align-items: baseline; justify-content: center; gap: 8px; font-weight: 700; }
  .step-bar .step-word { font-size: 9px; letter-spacing: 0.18em; }
  .label--cleanser .product-box { top: 288px; width: 200px; }
  .label--cleanser .product-name { height: 47px; font-size: 16px; }
  .label--cleanser .step-bar { height: 29px; font-size: 17px; padding-top: 5px; }
  .label--toner .product-box { top: 396px; width: 172px; }
  .label--toner .product-name { height: 42px; font-size: 13px; }
  .label--toner .step-bar { height: 24px; font-size: 14px; padding-top: 4px; }

  .claim { position: absolute; left: 0; right: 0; font-family: "Raleway", sans-serif; font-weight: 300; color: var(--text-grey); letter-spacing: 0.06em; }
  .label--cleanser .claim { top: 378px; font-size: 14px; line-height: 13px; }
  .label--toner .claim { top: 479px; font-size: 16px; line-height: 16px; }
  .volume { position: absolute; left: 0; right: 0; color: var(--ink); }
  .label--cleanser .volume { top: 420px; font-size: 18px; }
  .label--toner .volume { top: 528px; font-size: 13px; }

  /* brand block */
  .brand-mark { position: absolute; left: 853px; top: 72px; width: 160px; height: 160px; border: 4px solid var(--ink); border-radius: 50%; }
  .brand-wordmark { position: absolute; left: 681px; width: 497px; top: 275px; font-family: "Archivo Black", sans-serif; font-size: 58px; letter-spacing: 0.72em; text-indent: 0.72em; text-align: center; line-height: 1; }
  .brand-subbrand { position: absolute; left: 681px; width: 497px; top: 337px; font-size: 30px; font-weight: 800; letter-spacing: 0.14em; text-align: center; line-height: 1; }
  .brand-band { position: absolute; left: 681px; top: 383px; width: 497px; height: 89px; background: var(--ink); display: flex; align-items: center; justify-content: center; gap: 30px; }
  .brand-band .dot { width: 58px; height: 58px; border: 2px solid var(--tagline-teal); border-radius: 50%; }
  .brand-band .tagline { font-family: "Raleway", sans-serif; font-weight: 300; color: var(--tagline-teal); font-size: 29px; line-height: 1.12; }

  /* icon set */
  .icons-title { position: absolute; left: 868px; top: 552px; font-family: "Oswald", sans-serif; font-weight: 600; font-size: 30px; line-height: 1; }
  .icon { position: absolute; }
  .icon--teal-figure { left: 745px; top: 607px; width: 94px; height: 100px; background: linear-gradient(180deg, var(--icon-teal), var(--icon-blue)); border-radius: 45% 45% 50% 50%; }
  .icon--teal-lotus { left: 952px; top: 607px; width: 154px; height: 88px; background: linear-gradient(180deg, #a6d9cf, var(--icon-teal)); border-radius: 50% 50% 40% 40%; }
  .icon--outline-lotus { left: 720px; top: 747px; width: 142px; height: 90px; background: #e8e8e8; border-radius: 50% 50% 40% 40%; }
  .icon--outline-lotus-b { left: 966px; top: 750px; width: 124px; height: 82px; background: #e8e8e8; border-radius: 50% 50% 40% 40%; }
  .icon--drop { left: 877px; top: 866px; width: 68px; height: 93px; background: linear-gradient(160deg, #8fe0c6, var(--icon-teal) 50%, var(--icon-blue)); border-radius: 50% 50% 50% 50% / 40% 40% 60% 60%; }

  /* colour palette */
  .palette { position: absolute; left: 0; top: 996px; width: 1200px; height: 38px; display: flex; }
  .swatch { flex: 1; }
  .swatch--1 { background: var(--swatch-1); }
  .swatch--2 { background: var(--swatch-2); }
  .swatch--3 { background: var(--swatch-3); }
  .swatch--4 { background: var(--swatch-4); }
  .swatch--5 { background: var(--swatch-5); }
</style>
</head>
<body>
<main class="canvas">

  <section class="label label--cleanser" aria-label="Cleanser label">
    <div class="mark-circle"></div>
    <div class="wordmark">FABLE</div>
    <div class="subbrand">skin care</div>
    <div class="tag-band"><span class="dot"></span><p class="tagline">calm within<br>glow without</p></div>
    <p class="info">information line 1<br>information line 2</p>
    <div class="product-box">
      <div class="product-name">LULL CLEANSER</div>
      <div class="step-bar"><span class="step-word">STEP</span><span>01 02 03 04</span></div>
    </div>
    <p class="claim">natural<br>based<br>products</p>
    <p class="volume">00 oz</p>
  </section>

  <section class="label label--toner" aria-label="Toner label">
    <div class="mark-circle"></div>
    <div class="wordmark">FABLE</div>
    <div class="subbrand">skin care</div>
    <div class="tag-band"><span class="dot"></span><p class="tagline">calm within<br>glow without</p></div>
    <p class="info">information line 1<br>information line 2</p>
    <div class="product-box">
      <div class="product-name">HUSHWAY TONER</div>
      <div class="step-bar"><span class="step-word">STEP</span><span>01 02 03 04</span></div>
    </div>
    <p class="claim">natural<br>based<br>products</p>
    <p class="volume">00 oz</p>
  </section>

  <section class="brand" aria-label="Brand lockup">
    <div class="brand-mark"></div>
    <h1 class="brand-wordmark">FABLE</h1>
    <p class="brand-subbrand">skin care</p>
    <div class="brand-band"><span class="dot"></span><p class="tagline">calm within<br>glow without</p></div>
  </section>

  <section class="icon-set" aria-label="Icon set">
    <h2 class="icons-title">ICONS</h2>
    <div class="icon icon--teal-figure" role="img" aria-label="Teal gradient meditating figure icon with a droplet head"></div>
    <div class="icon icon--teal-lotus" role="img" aria-label="Layered teal lotus flower icon"></div>
    <div class="icon icon--outline-lotus" role="img" aria-label="Grey outline lotus flower icon"></div>
    <div class="icon icon--outline-lotus-b" role="img" aria-label="Grey outline multi-petal lotus icon"></div>
    <div class="icon icon--drop" role="img" aria-label="Teal and blue water droplet icon"></div>
  </section>

  <div class="palette" aria-label="Colour palette">
    <span class="swatch swatch--1"></span>
    <span class="swatch swatch--2"></span>
    <span class="swatch swatch--3"></span>
    <span class="swatch swatch--4"></span>
    <span class="swatch swatch--5"></span>
  </div>

</main>
</body>
</html>
```